Business Card Design for TrailStocked

TrailStocked is an online e-commerce store specializing in Outdoors Gear such as camping equipment, hunting and shooting equipment, tactical gear and more. See complete line at trailstocked.org
Logo: http://www.trailstocked.org/media/ID/Stocked.jpg
http://www.trailstocked.org/media/ID/TrailStocked-blue.jpg

Target Market(s)

20-40 Male

Industry/Entity Type

E-Commerce

```html
<!DOCTYPE html>
<html lang="en">
<head>
<meta charset="utf-8">
<title>TrailStocked Business Card</title>
<link rel="stylesheet" href="https://fonts.googleapis.com/css2?family=Noto+Serif:wght@700&family=Open+Sans:wght@400&family=Roboto+Condensed:wght@400;700&display=swap">
<style>
  :root {
    --backdrop: #b9b9bb;
    --navy: #212a51;
    --navy-mid: #2c365f;
    --haze: #7a809a;
    --white: #ffffff;
  }
  * { margin: 0; padding: 0; box-sizing: border-box; }
  html, body { width: 1200px; height: 900px; overflow: hidden; }
  body { background: var(--backdrop); position: relative; }

  .card {
    position: absolute;
    top: 285px;
    width: 508px;
    height: 329px;
    border-radius: 40px;
    overflow: hidden;
    color: var(--white);
  }
  .card--front {
    left: 62px;
    background: linear-gradient(112deg, var(--haze) 0%, var(--navy-mid) 38%, var(--navy) 62%, var(--navy) 100%);
  }
  .card--back {
    left: 630px;
    background: linear-gradient(248deg, var(--haze) 0%, #4a5275 30%, var(--navy) 58%, var(--navy) 100%);
  }

  .brand-ring {
    position: absolute;
    left: 48px;
    top: 128px;
    width: 66px;
    height: 66px;
    border: 2px solid var(--white);
    border-radius: 50%;
  }
  .wordmark {
    position: absolute;
    left: 128px;
    top: 134px;
    font-family: "Noto Serif", Georgia, serif;
    font-weight: 700;
    font-size: 37px;
    line-height: 1;
    letter-spacing: 0.6px;
  }
  .tagline {
    position: absolute;
    left: 129px;
    top: 178px;
    font-family: "Open Sans", Arial, sans-serif;
    font-size: 15.5px;
    letter-spacing: 2.1px;
    line-height: 1;
    white-space: nowrap;
  }

  .contact {
    position: absolute;
    left: 25px;
    top: 36px;
    font-family: "Roboto Condensed", Arial, sans-serif;
    font-size: 13px;
    line-height: 16.5px;
  }
  .contact__name {
    font-family: "Noto Serif", Georgia, serif;
    font-weight: 700;
    font-size: 16.5px;
    line-height: 19px;
  }
  .contact__group { margin-top: 17px; }

  .back-brand {
    position: absolute;
    left: 25px;
    top: 283px;
    font-family: "Roboto Condensed", Arial, sans-serif;
    font-weight: 700;
    font-size: 20px;
    line-height: 1;
  }
  .web {
    position: absolute;
    right: 46px;
    top: 286px;
    font-family: "Roboto Condensed", Arial, sans-serif;
    font-weight: 700;
    font-size: 20px;
    line-height: 1;
  }
</style>
</head>
<body>
  <section class="card card--front">
    <div class="brand-ring"></div>
    <div class="wordmark">TrailStocked.com</div>
    <div class="tagline">Outfitted for the Wild and the Road</div>
  </section>

  <section class="card card--back">
    <div class="contact">
      <div class="contact__name">Dorian Vellek</div>
      <div>Purchasing Manager</div>
      <div class="contact__group">
        <div>cell 847 555 0142</div>
        <div>office 847 555 0178</div>
      </div>
      <div class="contact__group">
        <div>PO BOX 728</div>
        <div>Ridgefield, IL 60012</div>
        <div>Purchasing@TrailStocked.org</div>
      </div>
    </div>
    <div class="back-brand">TrailStocked</div>
    <div class="web">www.TrailStocked.org</div>
  </section>
</body>
</html>
```